We need a brochure designed for each of our 4 online training schools. All content will be supplied and most of the graphics. We have just had our websites rebranded and brochure needs to reflect the same design/brand....so we have a very clear design look for you to follow. Each brochure version will have very similar content...just different logos, links and images.

Brochure needs to have a click through table of contents and links to website within it. Example of brochure attached. We need the first of these asap....but we will need 3 more versions based on exactly the same layout over the coming 2 weeks.

Payment is now for one editable version of brochure.  With both working and finished file to be sent to us.

Industry/Entity Type

Training

```html
<!DOCTYPE html>
<html lang="en">
<head>
<meta charset="UTF-8">
<title>Learning with Fieldstone</title>
<link href="https://fonts.googleapis.com/css2?family=Open+Sans:wght@400;600&display=swap" rel="stylesheet">
<style>
  :root {
    --coral: #f4876b;
    --coral-deep: #ea7659;
    --paper: #fdfcfb;
    --ink: #2e2e2e;
    --white: #ffffff;
    --photo-light: #e9e4da;
    --photo-mid: #a9b58c;
    --mark-bg: #ececec;
    --mark-ink: #666666;
  }
  * { margin: 0; padding: 0; box-sizing: border-box; }
  html, body { width: 1200px; height: 848px; overflow: hidden; }
  body {
    background: var(--paper);
    font-family: "Open Sans", sans-serif;
    color: var(--ink);
    position: relative;
  }
  .page-mark {
    position: absolute; left: 561px; top: 6px;
    height: 38px; display: flex; align-items: center; gap: 8px;
    background: var(--mark-bg); padding: 0 10px;
    font-size: 12px; color: var(--mark-ink);
  }
  .page-mark .brand { color: var(--coral-deep); font-weight: 600; font-size: 11px; }
  .page-mark .divider { width: 1px; height: 22px; background: var(--mark-ink); }
  .page-title {
    position: absolute; top: 68px; left: 0; width: 1200px;
    text-align: center; color: var(--coral);
    font-size: 35px; font-weight: 600; line-height: 44px;
  }
  .intro {
    position: absolute; top: 124px; left: 60px; width: 1072px;
    font-size: 14.6px; line-height: 21.5px; color: var(--ink);
  }
  .feature-band {
    position: absolute; top: 257px; left: 0; width: 1200px; height: 266px;
    background: var(--coral);
  }
  .feature-band svg { position: absolute; top: 0; left: 0; }
  .feature-photo {
    position: absolute; top: 257px; left: 402px; width: 400px; height: 266px;
    background: linear-gradient(160deg, var(--photo-mid) 0%, #c9ccb0 45%, var(--photo-light) 100%);
  }
  .courses {
    position: absolute; top: 540px; left: 0; width: 1200px;
  }
  .course {
    position: absolute; width: 220px; text-align: center;
    font-size: 13.6px; line-height: 19px;
  }
  .course .seal {
    display: block; width: 146px; height: 146px; margin: 0 auto 12px;
    border-radius: 50%; background: var(--coral);
  }
  .contact-bar {
    position: absolute; top: 772px; left: 0; width: 1200px; height: 76px;
    background: var(--coral);
  }
  .contact-item {
    position: absolute; top: 16px; width: 240px; text-align: center;
    color: var(--white); font-size: 12.5px; font-weight: 600;
  }
  .contact-item svg { display: block; margin: 0 auto 10px; }
</style>
</head>
<body>
  <div class="page-mark"><span class="brand">FIELDSTONE</span><span class="divider"></span><span>05</span></div>

  <h1 class="page-title">LEARNING WITH FIELDSTONE</h1>

  <p class="intro">Do you wish you could organize beautiful parties, corporate events and luxurious weddings? If you have a knack for planning and a creative mind, you can launch a career you'll love! You can learn from the comfort of your own home with one of Fieldstone Event School's four comprehensive programs. With each course, you'll learn from a combination of full color course texts, engaging video, hands-on assignments, and the support of your personal tutor. When you complete your course, you'll receive your graduation certificate. I'd like to welcome you to the School and to help you achieve your career goals. Please contact me with any questions you may have.</p>

  <section class="feature-band">
    <svg width="1200" height="266" viewBox="0 0 1200 266">
      <g fill="#ffffff">
        <rect x="164" y="0" width="13" height="266"/>
        <rect x="233" y="0" width="13" height="266"/>
        <rect x="282" y="0" width="13" height="266"/>
        <rect x="316" y="0" width="13" height="266"/>
        <rect x="341" y="0" width="13" height="266"/>
        <rect x="372" y="0" width="13" height="266"/>
        <rect x="816" y="0" width="13" height="266"/>
        <rect x="866" y="0" width="13" height="266"/>
        <rect x="906" y="0" width="13" height="266"/>
        <rect x="952" y="0" width="13" height="266"/>
        <rect x="1022" y="0" width="13" height="266"/>
      </g>
    </svg>
  </section>
  <div class="feature-photo" role="img" aria-label="Photo of an event planner with a tablet talking with a bride at an outdoor wedding reception"></div>

  <section class="courses">
    <div class="course" style="left:39px;"><span class="seal"></span>Fieldstone Event &amp;<br>Wedding Planning<br>Diploma course<br>EWPD</div>
    <div class="course" style="left:339px;"><span class="seal"></span>Fieldstone<br>Event Planning<br>Diploma course<br>EPPD</div>
    <div class="course" style="left:641px;"><span class="seal"></span>Fieldstone Wedding<br>Planning Diploma<br>course WPPD</div>
    <div class="course" style="left:940px;"><span class="seal"></span>Fieldstone Event<br>Styling Diploma<br>course ESDD</div>
  </section>

  <footer class="contact-bar">
    <div class="contact-item" style="left:289px;">
      <svg width="16" height="16" viewBox="0 0 16 16"><circle cx="8" cy="8" r="8" fill="#fff"/><rect x="4" y="5" width="8" height="6" fill="none" stroke="#f4876b" stroke-width="1.2"/><path d="M4 5 L8 8.5 L12 5" fill="none" stroke="#f4876b" stroke-width="1.2"/></svg>
      mara@fieldstone-academy.co.uk
    </div>
    <div class="contact-item" style="left:502px;">
      <svg width="16" height="16" viewBox="0 0 16 16"><circle cx="8" cy="8" r="8" fill="#fff"/><path d="M5.2 4.2 L6.6 4 L7.3 6 L6.4 6.8 Q7.2 8.6 9.1 9.6 L9.9 8.7 L11.9 9.4 L11.7 10.8 Q8.8 11.4 6.7 9.2 Q4.6 7 5.2 4.2 Z" fill="#f4876b"/></svg>
      0800 555 0142.
    </div>
    <div class="contact-item" style="left:716px;">
      <svg width="16" height="16" viewBox="0 0 16 16"><circle cx="8" cy="8" r="8" fill="#fff"/><circle cx="8" cy="8" r="3.5" fill="none" stroke="#f4876b" stroke-width="1.3"/></svg>
    </div>
  </footer>
</body>
</html>
```